Target Market(s)

audience is people who search for a life coaching and a consultation at a certain point in their lives.

Industry/Entity Type

Consulting

Number of Pages Required

1 page

Requirements
Must have
• the heading must fit in top of the website and must be changeable.

• THE DESIGN MUST BE UNIQUE AND NO EXISTING TEMPLATE AND NOT BE BASED ON AN EXISTING TEMPLATE.
Nice to have
• maybe a small logo next to the heading.

```html
<!DOCTYPE html>
<html lang="en">
<head>
<meta charset="utf-8">
<title>Life Coach</title>
<link href="https://fonts.googleapis.com/css2?family=Arimo:wght@400;700&family=Tinos&display=swap" rel="stylesheet">
<style>
:root{
  --brand:#17a6cc;
  --ink:#000;
  --muted:#777;
  --rule:#dcdcdc;
  --dots:#b5b5b5;
  --ph-cool:#cfe3ee;
  --ph-warm:#dfe8c8;
}
*{margin:0;padding:0;box-sizing:border-box}
html,body{width:1127px;height:1200px;overflow:hidden;background:#fff}
body{position:relative;font-family:"Arimo",Arial,sans-serif;color:var(--ink)}
.abs{position:absolute}
.brand{left:46px;top:22px;display:flex;align-items:center;gap:12px}
.brand-dot{width:22px;height:22px;border-radius:50%;background:var(--brand)}
.brand-name{font-family:"Tinos",serif;font-size:46px;color:var(--brand);line-height:1}
.brand-rule{left:370px;top:75px;width:670px;height:1px;background:var(--brand)}
.placeholder{background:linear-gradient(135deg,var(--ph-cool),var(--ph-warm))}
.hero{left:40px;top:100px;width:1000px;height:342px}
.nav{left:40px;top:451px;width:1000px;height:56px}
.nav a{position:absolute;top:0;height:56px;line-height:56px;font-family:"Tinos",serif;font-size:19px;color:var(--ink);text-decoration:none;text-align:center}
.nav a.active{background:var(--brand);color:#fff}
.nav .sep{position:absolute;top:0;width:1px;height:56px;background:var(--rule)}
.hr{height:1px;background:var(--rule)}
.vr{width:1px;background:var(--rule)}
.col-title{font-family:"Tinos",serif;font-weight:400;font-size:24px;top:574px;white-space:nowrap}
.col-title b{font-weight:400;font-size:30px}
.news-thumb{width:111px;height:98px}
.news-date{font-size:12px;font-weight:700;letter-spacing:.5px}
.news-text{font-size:12px;color:var(--muted);line-height:18px;white-space:nowrap;letter-spacing:.2px}
.more{font-size:12px;font-weight:700;color:var(--brand);letter-spacing:.8px}
.welcome-img{left:385px;top:646px;width:300px;height:112px}
.welcome-text{left:381px;top:784px;font-size:12px;color:var(--muted);line-height:20px;white-space:nowrap}
.welcome-text strong{color:var(--ink);letter-spacing:.3px}
.welcome-text p+p{margin-top:20px}
.events{left:757px;top:634px;width:283px;list-style:none}
.events li{height:36px;border-bottom:1px dotted var(--dots);display:flex;align-items:center;gap:13px;font-size:12px;color:var(--muted)}
.events li:last-child{border-bottom:none}
.events svg{flex:none}
.link-all{top:1021px;font-size:12px;font-weight:700;letter-spacing:.5px}
.footer{top:1094px;font-size:12px}
.footer-nav span{margin:0 6px}
</style>
</head>
<body>
<header>
  <div class="abs brand"><span class="brand-dot"></span><span class="brand-name">Life Coach</span></div>
  <div class="abs brand-rule"></div>
  <div class="abs hero placeholder" role="img" aria-label="Hero photo: joyful woman with open arms in an open meadow, with the tagline Make your life well"></div>
  <nav class="abs nav">
    <a class="active" style="left:65px;width:141px">Home</a>
    <a style="left:240px;width:120px">About Us</a>
    <span class="sep" style="left:376px"></span>
    <a style="left:420px;width:140px">Our Services</a>
    <span class="sep" style="left:594px"></span>
    <a style="left:633px;width:120px">Our Mission</a>
    <span class="sep" style="left:809px"></span>
    <a style="left:828px;width:120px">Contact Us</a>
  </nav>
  <div class="abs hr" style="left:40px;top:517px;width:1000px"></div>
</header>

<main>
  <div class="abs vr" style="left:351px;top:560px;height:440px"></div>
  <div class="abs vr" style="left:727px;top:560px;height:440px"></div>
  <h2 class="abs col-title" style="left:40px"><b>Latest</b> news</h2>
  <h2 class="abs col-title" style="left:380px"><b>Welcome</b> to our site</h2>
  <h2 class="abs col-title" style="left:756px"><b>Upcoming</b> events</h2>
  <div class="abs hr" style="left:40px;top:619px;width:1000px"></div>

  <section>
    <div class="abs news-thumb placeholder" style="left:41px;top:648px" role="img" aria-label="Photo of a smiling young woman outdoors"></div>
    <div class="abs news-date" style="left:165px;top:648px">Jan,18,2010</div>
    <p class="abs news-text" style="left:165px;top:673px">Lorem ipsum dolor sit amet,<br>consetetur sadipscing elitr,<br>sed diam nonumy eirmod</p>
    <a class="abs more" style="left:166px;top:735px">more...</a>

    <div class="abs news-thumb placeholder" style="left:41px;top:769px" role="img" aria-label="Photo of friends throwing autumn leaves"></div>
    <div class="abs news-date" style="left:165px;top:768px">Mar,04,2010</div>
    <p class="abs news-text" style="left:165px;top:792px">Lorem ipsum dolor sit amet,<br>consetetur sadipscing elitr,<br>sed diam nonumy eirmod</p>
    <a class="abs more" style="left:166px;top:857px">more...</a>

    <div class="abs news-thumb placeholder" style="left:41px;top:891px" role="img" aria-label="Photo of two smiling girls giving a thumbs up"></div>
    <div class="abs news-date" style="left:165px;top:892px">Jan,18,2010</div>
    <p class="abs news-text" style="left:165px;top:917px">Lorem ipsum dolor sit amet,<br>consetetur sadipscing elitr,<br>sed diam nonumy eirmod</p>
    <a class="abs more" style="left:166px;top:980px">more...</a>
  </section>

  <section>
    <div class="abs welcome-img placeholder" role="img" aria-label="Photo of three women walking hand in hand outdoors"></div>
    <div class="abs welcome-text">
      <p><strong>Lorem ipsum dolor sit amet, consetetur sadipsc-<br>ing elitr, sed diam nonumy eirmod</strong> tempor invidunt<br>ut labore et dolore magna aliquyam erat, sed. At vero eos<br>erat, sed diam voluptua.et ea rebum.eirmod tempor invid-<br>unt ut labore et dolore magna aliquyam erat, sed diam<br>voluptua.</p>
      <p>Lorem ipsum dolor sit amet, consetetur sadipscing<br>elitr.sed diam nonumy eirmod tempor invidunt ut labore et<br>dolore magna aliquyam erat, sed diam voluptua.et ea<br>rebum.eirmod tempor invidunt dolor sit</p>
    </div>
  </section>

  <section>
    <ul class="abs events">
      <li><svg width="11" height="11" viewBox="0 0 11 11"><rect width="11" height="11" rx="2" fill="var(--brand)"/><path d="M4 2.5 7 5.5 4 8.5" stroke="#fff" stroke-width="1.6" fill="none"/></svg>Lorem ipsum dolor sit amet, consetetur</li>
      <li><svg width="11" height="11" viewBox="0 0 11 11"><rect width="11" height="11" rx="2" fill="var(--brand)"/><path d="M4 2.5 7 5.5 4 8.5" stroke="#fff" stroke-width="1.6" fill="none"/></svg>Sscing elitr, sed diam nonumy eirmod tempor</li>
      <li><svg width="11" height="11" viewBox="0 0 11 11"><rect width="11" height="11" rx="2" fill="var(--brand)"/><path d="M4 2.5 7 5.5 4 8.5" stroke="#fff" stroke-width="1.6" fill="none"/></svg>invidunt ut labore et dolore magna aliquyam</li>
      <li><svg width="11" height="11" viewBox="0 0 11 11"><rect width="11" height="11" rx="2" fill="var(--brand)"/><path d="M4 2.5 7 5.5 4 8.5" stroke="#fff" stroke-width="1.6" fill="none"/></svg>At vero eos erat, sed diam voluptuaeos erat.</li>
      <li><svg width="11" height="11" viewBox="0 0 11 11"><rect width="11" height="11" rx="2" fill="var(--brand)"/><path d="M4 2.5 7 5.5 4 8.5" stroke="#fff" stroke-width="1.6" fill="none"/></svg>Eirmod tempor invidunt ut labore et dolore</li>
      <li><svg width="11" height="11" viewBox="0 0 11 11"><rect width="11" height="11" rx="2" fill="var(--brand)"/><path d="M4 2.5 7 5.5 4 8.5" stroke="#fff" stroke-width="1.6" fill="none"/></svg>Magna aliquyam erat, sed diam voluptua.</li>
      <li><svg width="11" height="11" viewBox="0 0 11 11"><rect width="11" height="11" rx="2" fill="var(--brand)"/><path d="M4 2.5 7 5.5 4 8.5" stroke="#fff" stroke-width="1.6" fill="none"/></svg>Lorem ipsum dolor sit amet, consetetur sadi.</li>
      <li><svg width="11" height="11" viewBox="0 0 11 11"><rect width="11" height="11" rx="2" fill="var(--brand)"/><path d="M4 2.5 7 5.5 4 8.5" stroke="#fff" stroke-width="1.6" fill="none"/></svg>Sed diam nonumy eirmod tempor invidunt</li>
      <li><svg width="11" height="11" viewBox="0 0 11 11"><rect width="11" height="11" rx="2" fill="var(--brand)"/><path d="M4 2.5 7 5.5 4 8.5" stroke="#fff" stroke-width="1.6" fill="none"/></svg>Labore et dolore magna aliquyam erat.</li>
      <li><svg width="11" height="11" viewBox="0 0 11 11"><rect width="11" height="11" rx="2" fill="var(--brand)"/><path d="M4 2.5 7 5.5 4 8.5" stroke="#fff" stroke-width="1.6" fill="none"/></svg>Diam voluptua.et ea rebum.eirmod tempor</li>
    </ul>
  </section>

  <a class="abs link-all" style="left:40px">More News...</a>
  <a class="abs link-all" style="left:385px">Read more...</a>
  <a class="abs link-all" style="left:756px">All events...</a>
</main>

<footer>
  <div class="abs hr" style="left:40px;top:1056px;width:1000px"></div>
  <p class="abs footer" style="left:41px">All Rights Reserved 2010. Life Coach</p>
  <p class="abs footer footer-nav" style="right:86px">Home<span>|</span>Services<span>|</span>Events<span>|</span>Contact us</p>
</footer>
</body>
</html>
```